Business Cards Needed For Veterinary Business

Looking for a business card design for a veterinary blood bank. We would like it to be clean and professional on appearance but still warm and inviting. We would like to utilize our logo and similar coloring. We will use our phone number, email, website, employee name, employee title.

We do not want a bunch of animated animal photos but do not need the style to be as clinical as a laboratory or human medical procedure office.

We are looking for some creative ideas to choose from so that we can generate a standout professional business card for our management team to utilize.

Target Market(s)

professionals

Industry/Entity Type

veterinary

Contact Information for Business Card

employee name, employee title, phone number, website URL, email

Font styles to use
Sans Serif

Colors
0054AA
0677BA
7BADD7
CADEEF
E8F1F8
EB3D1F
EC4F4E
F09395
F8D3D4
FCEDEE

Requirements
Nice to have
• creative design
Should not have
• animated photos

```html
<!DOCTYPE html>
<html lang="en">
<head>
<meta charset="utf-8">
<title>Meridian Animal Blood Bank – Business Cards</title>
<link href="https://fonts.googleapis.com/css2?family=Montserrat:wght@400;600;800&display=swap" rel="stylesheet">
<style>
  :root{
    --stage:#151515;
    --charcoal:#333333;
    --blue-deep:#0b4a98;
    --blue:#0054AA;
    --blue-mid:#0a60b0;
    --blue-shade:#0a4688;
    --red:#EB3D1F;
    --red-bright:#e8202a;
    --white:#ffffff;
  }
  *{margin:0;padding:0;box-sizing:border-box}
  html,body{width:1200px;height:963px;overflow:hidden;background:var(--stage);font-family:"Montserrat",Arial,sans-serif}
  .stage{position:relative;width:1200px;height:963px}
  .card{position:absolute;top:333px;width:520px;height:297px;border-radius:22px;overflow:hidden;box-shadow:0 14px 30px rgba(0,0,0,.55)}
  .card--front{left:50px;background:var(--blue-mid)}
  .card--back{left:630px;background:linear-gradient(135deg,var(--blue-deep),var(--blue) 55%,var(--blue-mid))}
  .front__top{position:absolute;inset:0;background:var(--charcoal);clip-path:polygon(0 0,100% 0,100% 82%,0 52%)}
  .front__divider{position:absolute;inset:0;width:100%;height:100%}
  .brand{position:absolute;font-weight:800;line-height:1;letter-spacing:.5px;text-transform:uppercase}
  .brand__short{display:block;font-size:58px;letter-spacing:1px}
  .brand__long{display:block;font-size:14.5px;margin-top:6px}
  .card--front .brand{left:38px;top:26px;color:var(--red-bright)}
  .card--back .brand{left:42px;top:40px;color:var(--white)}
  .person{position:absolute;left:38px;top:112px;color:var(--white)}
  .person__name{font-weight:800;font-size:17px;letter-spacing:.5px;color:var(--red-bright);text-transform:uppercase}
  .person__title{font-size:12px;margin-top:3px}
  .contact{position:absolute;left:30px;top:198px;list-style:none;color:var(--white);font-size:13.5px}
  .contact li{display:flex;align-items:center;gap:8px;margin-bottom:6px}
  .contact svg{width:13px;height:13px;flex:none}
  .mark-area{position:absolute;border-radius:26px}
  .card--front .mark-area{left:330px;top:120px;width:150px;height:160px;background:linear-gradient(160deg,#f0333a,var(--red-bright))}
  .card--back .mark-area{left:320px;top:110px;width:170px;height:170px;background:linear-gradient(160deg,var(--blue-shade),#0d58a8);opacity:.85}
</style>
</head>
<body>
<main class="stage">
  <article class="card card--front">
    <div class="front__top"></div>
    <svg class="front__divider" viewBox="0 0 520 297" preserveAspectRatio="none" aria-hidden="true">
      <line x1="0" y1="155" x2="520" y2="243" stroke="var(--red-bright)" stroke-width="3"/>
    </svg>
    <div class="mark-area" role="img" aria-label="Brand emblem area in red"></div>
    <div class="brand">
      <span class="brand__short">MABB</span>
      <span class="brand__long">Meridian Animal Blood Bank</span>
    </div>
    <div class="person">
      <p class="person__name">Daniel Reyes</p>
      <p class="person__title">Manager</p>
    </div>
    <ul class="contact">
      <li><svg viewBox="0 0 24 24" fill="none" stroke="#fff" stroke-width="2"><path d="M5 3h4l2 5-3 2a12 12 0 0 0 6 6l2-3 5 2v4a2 2 0 0 1-2 2A18 18 0 0 1 3 5a2 2 0 0 1 2-2z"/></svg>555-014-2100</li>
      <li><svg viewBox="0 0 24 24" fill="none" stroke="#fff" stroke-width="2"><rect x="2" y="5" width="20" height="14" rx="1"/><path d="M2 6l10 7 10-7"/></svg>hello@mabbvet.org</li>
      <li><svg viewBox="0 0 24 24" fill="none" stroke="#fff" stroke-width="2"><circle cx="12" cy="12" r="10"/><path d="M2 12h20M12 2c3 3 3 17 0 20M12 2c-3 3-3 17 0 20"/></svg>www.mabbvet.org</li>
    </ul>
  </article>

  <article class="card card--back">
    <div class="mark-area" role="img" aria-label="Faint embossed brand emblem area in blue"></div>
    <div class="brand">
      <span class="brand__short">MABB</span>
      <span class="brand__long">Meridian Animal Blood Bank</span>
    </div>
  </article>
</main>
</body>
</html>
```